Website Graphic Layout

We are looking for someone to provide a crisp clean layout for our new website design.
The site is runs on Drupal & we like the 4 column layout
We think that the current site is a bit cluttered & could be a bit cleaner.

http://www.brovantel.org/volunteer-abroad

We like the following website as examples as they are quite clean with a large header image & sub areas to add things such as news testimonials etc

http://quindrax.com/
http://www.zorpat.com/ie/
http://harbelwing.org/
http://www.velkori.com/

Industry/Entity Type

Cleaner

```html
<!DOCTYPE html>
<html lang="en">
<head>
<meta charset="utf-8">
<title>Brovantel Intercultural Learning</title>
<link href="https://fonts.googleapis.com/css2?family=Arimo:wght@400;700&family=Open+Sans:wght@400&display=swap" rel="stylesheet">
<style>
:root{
  --green:#12a23c;
  --green-light:#6fd07a;
  --green-dark:#0b7f2c;
  --logo-green:#1a9a3c;
  --orange:#f39200;
  --navy:#2a3a7a;
  --magenta:#e8217a;
  --photo:#7a7a7a;
  --hero-red:#b9453e;
  --footer-bg:#e3e3e3;
  --footer-text:#3cb54a;
  --ink:#222;
  --white:#fff;
}
*{margin:0;padding:0;box-sizing:border-box}
html,body{width:1200px;height:1006px;overflow:hidden;background:var(--white)}
body{font-family:"Arimo",Arial,sans-serif}
.page{position:relative;width:1000px;height:838px;transform:scale(1.2);transform-origin:0 0}
.abs{position:absolute;white-space:nowrap}

.topbar{left:0;top:0;width:1000px;height:33px;background:linear-gradient(180deg,var(--green-light),var(--green));box-shadow:0 2px 3px rgba(0,0,0,.25)}
.social{top:9px;width:20px;height:20px;border-radius:50%;background:#dfe6ef;border:2px solid #c6ccd6}
.topnav{top:12px;color:var(--white);font-weight:700;font-size:12px;letter-spacing:.2px}
.search{left:660px;top:12px;width:137px;height:15px;border-radius:5px;background:var(--white);font-size:7.5px;font-weight:700;padding:3px 0 0 16px;color:var(--ink)}

.logo{left:218px;top:52px;font-size:38px;color:var(--logo-green);letter-spacing:-1px}
.welcome{left:349px;top:44px;width:104px;height:29px;background:var(--orange);color:var(--white);font-size:8px;font-weight:700;line-height:8px;padding:3px 6px;border-radius:2px;white-space:normal}
.phone{top:44px;height:29px;background:linear-gradient(180deg,var(--green-light),var(--green));color:var(--white);font-weight:700;font-size:12px;padding:8px 0 0 10px;border-radius:2px;box-shadow:1px 1px 2px rgba(0,0,0,.3)}
.menu{left:349px;top:81px;width:449px;height:21px;background:linear-gradient(180deg,#3cc25a,var(--green-dark));display:flex;border-radius:2px;box-shadow:1px 1px 2px rgba(0,0,0,.3);overflow:hidden}
.menu span{color:var(--white);font-size:8.6px;font-weight:700;line-height:21px;text-align:center;white-space:nowrap;border-right:1px solid rgba(255,255,255,.6)}
.menu span:last-child{border:none}

.hero-band{left:200px;width:600px}
.hero-photo{left:200px;top:125px;width:600px;height:220px;background:linear-gradient(100deg,#5b4a43,var(--hero-red) 45%,#8b6f5a 75%,#6a5a50)}
.news-panel{left:526px;top:148px;width:250px;height:175px;background:rgba(235,235,235,.45);border-radius:4px;color:rgba(255,255,255,.85);font-size:31px;font-weight:700;text-align:center;padding-top:75px}
.caption{left:222px;top:297px;width:277px;height:27px;background:#141414;font-size:10px;font-weight:700;padding-top:9px}
.caption .label{position:absolute;left:8px;color:#bdbdbd}
.caption .more{position:absolute;right:12px;color:var(--orange)}
.rule{left:200px;top:364px;width:600px;height:1px;background:#c8c8c8}

.col-title{top:390px;font-size:9px;font-weight:700}
.card{top:416px;width:124px;height:199px;border:1px solid #8fd49a;background:var(--white)}
.card .photo{height:100px;background:var(--photo);color:var(--white);font-size:9.5px;text-align:center;padding-top:45px}
.card .text{text-align:center;color:#777;font-size:11.5px;padding-top:47px}
.card .view{position:absolute;right:-1px;bottom:-1px;width:40px;height:14px;background:var(--orange);color:var(--ink);font-size:7.5px;font-weight:700;padding:3px 0 0 6px}

.footer{left:0;top:658px;width:1000px;height:180px;background:var(--footer-bg);border-top:2px solid var(--green)}
.flink{font-family:"Open Sans",sans-serif;font-size:11.4px;color:var(--footer-text);line-height:12px}
.flink.wrap{white-space:normal}
.footer-rule{left:0;top:777px;width:1000px;height:1px;background:#b5b5b5}
.legal{left:213px;top:784px;font-size:8.3px;line-height:12.5px;color:var(--ink)}
.footer-logo{left:686px;top:786px;font-size:30px;font-weight:700;color:var(--logo-green)}
</style>
</head>
<body>
<div class="page">
  <header class="abs topbar"></header>
  <span class="abs social" style="left:206px"></span>
  <span class="abs social" style="left:235px"></span>
  <span class="abs social" style="left:263px"></span>
  <span class="abs social" style="left:290px"></span>
  <span class="abs topnav" style="left:335px">VISIT IRELAND</span>
  <span class="abs topnav" style="left:430px">|</span>
  <span class="abs topnav" style="left:450px">ABOUT BVT</span>
  <span class="abs topnav" style="left:525px">|</span>
  <span class="abs topnav" style="left:545px">COMMUNITY</span>
  <div class="abs search">SEARCH...</div>

  <div class="abs logo">LOGO</div>
  <div class="abs welcome">WELCOME GUEST.<br>LOGIN, REGISTER.<br>CONTACT US.</div>
  <div class="abs phone" style="left:456px;width:169px">LOCALL: 1850 418273</div>
  <div class="abs phone" style="left:628px;width:170px">TELEPHONE: 021 4609827</div>
  <nav class="abs menu">
    <span style="width:42px">HOME</span><span style="width:80px">STUDY ABROAD</span><span style="width:104px">VOLUNTEER ABROAD</span><span style="width:130px">DEVELOPMENT EDUCATION</span><span style="width:93px">TRAVEL AWARDS</span>
  </nav>

  <svg class="abs hero-band" style="top:114px" width="600" height="12" viewBox="0 0 600 12">
    <path d="M0 12 V2 Q300 -2 600 2 V12 Z" fill="#1aa63e"/>
    <path d="M0 4 Q300 0 600 4" stroke="#9be3a6" stroke-width="1.5" fill="none"/>
  </svg>
  <div class="abs hero-photo" role="img" aria-label="Volunteers and local children gathered together at a community event"></div>
  <div class="abs news-panel">NEWS</div>
  <div class="abs caption"><span class="label">VOLUNTEER ABROAD</span><span class="more">NEWS AND EVENT →</span></div>
  <svg class="abs hero-band" style="top:344px" width="600" height="12" viewBox="0 0 600 12">
    <path d="M0 0 V8 Q300 13 600 8 V0 Z" fill="#1aa63e"/>
  </svg>
  <div class="abs rule"></div>

  <div class="abs col-title" style="left:210px;color:var(--green)">→&nbsp;&nbsp;&nbsp;FEATURED PROGRAMME</div>
  <div class="abs col-title" style="left:366px;color:var(--navy)">→&nbsp;&nbsp;&nbsp;NEWS AND EVENTS</div>
  <div class="abs col-title" style="left:526px;color:var(--magenta)">→&nbsp;&nbsp;&nbsp;TESTIMONIALS</div>
  <div class="abs col-title" style="left:672px;color:var(--magenta)">→&nbsp;&nbsp;&nbsp;FEATURED VIDEOS</div>

  <div class="abs card" style="left:214px"><div class="photo">PHOTO</div><div class="text">TEXT</div><div class="view">VIEW →</div></div>
  <div class="abs card" style="left:363px"><div class="photo">PHOTO</div><div class="text">TEXT</div><div class="view">VIEW →</div></div>
  <div class="abs card" style="left:513px"><div class="photo">PHOTO</div><div class="text">TEXT</div><div class="view">VIEW →</div></div>
  <div class="abs card" style="left:664px"><div class="photo">PHOTO</div><div class="text">TEXT</div><div class="view">VIEW →</div></div>

  <footer class="abs footer"></footer>
  <span class="abs flink" style="left:217px;top:683px">Countries &nbsp;⟶</span>
  <span class="abs flink" style="left:217px;top:708px">Fin your project</span>
  <span class="abs flink" style="left:217px;top:733px">Under 18- programme</span>
  <span class="abs flink" style="left:217px;top:758px">Internship programme</span>
  <span class="abs flink" style="left:349px;top:683px">Corporate Volunting &nbsp;⟶</span>
  <span class="abs flink" style="left:349px;top:708px">School Programme</span>
  <span class="abs flink" style="left:349px;top:733px">Fundraising</span>
  <span class="abs flink" style="left:349px;top:758px">News</span>
  <span class="abs flink" style="left:505px;top:683px">Why BVT? &nbsp;⟶</span>
  <span class="abs flink" style="left:505px;top:708px">Is this for me?</span>
  <span class="abs flink" style="left:505px;top:733px">Why Pay?</span>
  <span class="abs flink" style="left:505px;top:758px">How do i apply?</span>
  <span class="abs flink" style="left:651px;top:683px">FAQ</span>
  <span class="abs flink" style="left:651px;top:708px">About us</span>
  <span class="abs flink" style="left:651px;top:733px">Contact us</span>
  <span class="abs flink wrap" style="left:651px;top:752px;width:160px">Discover our 5 most popular destinations</span>
  <div class="abs footer-rule"></div>
  <div class="abs legal">Brovantel Intercultural Learning, 4 Larchfield Row, Millbrook East, Cork, County Cork, Republic of Ireland.<br>email: info@brovantel.org telephone: +353 (0)21 4609827 lowcall: 1850 418273 fax: +353 (0)21 4609840<br>cc by-sa 2013 Brovantel Intercultural Learning</div>
  <div class="abs footer-logo">LOGO</div>
</div>
</body>
</html>
```